new business card design - modern, professional, bold, B2B focus - with QR code pls

we are looking for a modern looking, colorful, business card design. some highlights:
- put space for QR code please. probably on the back but I'm open.
- biz card to be orientated VERTICAL not the traditional horizontal.
- do NOT use our full name on the card (ie: Allied Furnace Servicing Inc). Use only AFS Inc or AFS.
- use black and orange with some white. ideally black card with orange and white for the letters/logo etc. gray ok too - for outlines etc.
- we work in HEAVY industrial, so the cards should lend itself to this. our website is alfurnace.example, so you can see what we do.
- do NOT put in little smoke stack pictures / silouettes etc.
- think MODERN and INDUSTRIAL, with a techy focus.

Industry/Entity Type

heavy industrial - all of them. we perform maintenance and inspection services at heavy industrial and commercial businesses. so B2B

Contact Information for Business Card

name, title, phone numbers (cell + hardline), website, email address. of course our logo too - either on front or front and back.

Font styles to use
Other font styles liked:
• montserrat

Colors
F0912C
F2A743
F7CA91
FBE8D2
FDF5EE

Requirements
Must have
• see description
Nice to have
• see description
Should not have
• see description

```html
<!DOCTYPE html>
<html lang="en">
<head>
<meta charset="utf-8">
<title>AFS Inc – Business Card</title>
<link rel="stylesheet" href="https://fonts.googleapis.com/css2?family=Montserrat:wght@400;500;700;800&display=swap">
<style>
  :root {
    --card-black: #231f20;
    --orange: #f0912c;
    --orange-deep: #6e3f02;
    --orange-mid: #b06a0c;
    --white: #ffffff;
    --soft-white: #f2f2f2;
    --rule: #9a5e15;
    --page: #5a5a5c;
  }
  * { box-sizing: border-box; margin: 0; padding: 0; }
  html, body { width: 1200px; height: 900px; overflow: hidden; }
  body {
    background: var(--page);
    font-family: "Montserrat", sans-serif;
    position: relative;
  }
  .card {
    position: absolute;
    top: 120px;
    width: 380px;
    height: 660px;
    overflow: hidden;
  }

  /* Front */
  .card-front {
    left: 170px;
    background: var(--card-black);
    border-radius: 48px 0 48px 0;
    color: var(--white);
  }
  .brand-mark {
    position: absolute;
    left: 42px;
    top: 60px;
    display: flex;
    align-items: center;
    gap: 14px;
  }
  .brand-mark .dot {
    width: 22px; height: 22px;
    background: var(--orange);
  }
  .brand-mark .name {
    font-weight: 800;
    font-size: 72px;
    letter-spacing: 1px;
    color: var(--orange);
    line-height: 1;
  }
  .identity {
    position: absolute;
    left: 42px;
    top: 330px;
  }
  .identity .title {
    font-size: 17px;
    font-weight: 400;
    color: var(--white);
  }
  .identity .person {
    font-size: 24px;
    font-weight: 800;
    color: var(--orange);
    margin-top: 2px;
    letter-spacing: .5px;
  }
  .contact-group {
    position: absolute;
    left: 42px;
    right: 30px;
    border-top: 1.5px solid var(--rule);
    padding-top: 14px;
  }
  .contact-phones { top: 418px; border-top: none; padding-top: 0; }
  .contact-web { top: 490px; }
  .contact-address { top: 575px; font-size: 15px; line-height: 1.4; }
  .contact-line {
    display: flex;
    align-items: center;
    gap: 10px;
    font-size: 15.5px;
    line-height: 1.7;
  }
  .contact-line svg { width: 16px; height: 16px; flex: none; }
  .phones-block { padding-bottom: 12px; }

  /* Back */
  .card-back {
    left: 650px;
    border-radius: 0 48px 0 48px;
    background: linear-gradient(160deg, var(--orange-deep) 0%, var(--orange-mid) 50%, var(--orange) 100%);
  }
  .back-url {
    position: absolute;
    left: 26px;
    top: 34px;
    writing-mode: vertical-rl;
    transform: rotate(180deg);
    font-size: 15px;
    font-weight: 500;
    letter-spacing: 4px;
    color: var(--white);
  }
  .qr-space {
    position: absolute;
    left: 200px;
    top: 60px;
    width: 130px;
    height: 130px;
    border: 2px dashed rgba(255, 255, 255, .75);
    border-radius: 8px;
    background: rgba(255, 255, 255, .12);
  }
  .back-brand {
    position: absolute;
    right: 40px;
    bottom: 110px;
    font-weight: 800;
    font-size: 120px;
    line-height: 1;
    color: var(--soft-white);
  }
</style>
</head>
<body>
  <section class="card card-front" aria-label="Card front">
    <div class="brand-mark">
      <span class="dot"></span>
      <span class="name">AFS</span>
    </div>

    <div class="identity">
      <p class="title">CEO &amp; Director</p>
      <p class="person">DALE MARSH</p>
    </div>

    <div class="contact-group contact-phones">
      <p class="contact-line">
        <svg viewBox="0 0 16 16" fill="none" stroke="#f0912c" stroke-width="1.5"><rect x="4" y="1.5" width="8" height="13" rx="1.5"/><line x1="7" y1="12" x2="9" y2="12"/></svg>
        555-214-7730
      </p>
      <p class="contact-line phones-block">
        <svg viewBox="0 0 16 16" fill="#f0912c"><path d="M3 1.5l3 .5 1 3-2 1.3a8 8 0 0 0 4.7 4.7L11 9l3 1 .5 3-2 1.5C6.5 14 2 9.5 1.5 3.5z"/></svg>
        877-FURNACE
      </p>
    </div>

    <div class="contact-group contact-web">
      <p class="contact-line">
        <svg viewBox="0 0 16 16" fill="#f0912c"><path d="M1 3h14v10H1z"/><path d="M1 3l7 6 7-6" stroke="#231f20" stroke-width="1.3" fill="none"/></svg>
        afsinc@alfurnace.example
      </p>
      <p class="contact-line">
        <svg viewBox="0 0 16 16" fill="none" stroke="#f0912c" stroke-width="1.3"><circle cx="8" cy="8" r="6.5"/><ellipse cx="8" cy="8" rx="3" ry="6.5"/><line x1="1.5" y1="8" x2="14.5" y2="8"/></svg>
        alfurnace.example
      </p>
    </div>

    <div class="contact-group contact-address">
      <p>4210 Mill Quarry Road, Unit #2</p>
      <p>Ashford, On L0h 2k0, Canada</p>
    </div>
  </section>

  <section class="card card-back" aria-label="Card back">
    <p class="back-url">alfurnace.example</p>
    <div class="qr-space" role="img" aria-label="Reserved space for QR code linking to alfurnace.example"></div>
    <p class="back-brand">AFS</p>
  </section>
</body>
</html>
```